- Redesign our business card
- Logo remains unchanged
- Current business card attached

Target Market(s)

We are a property management company

Industry/Entity Type

Business

```html
<!DOCTYPE html>
<html lang="en">
<head>
<meta charset="utf-8">
<title>Harlow Property Group – Business Card</title>
<link rel="stylesheet" href="https://fonts.googleapis.com/css2?family=Jost:wght@400;500;600&display=swap">
<style>
  :root {
    --page: #ffffff;
    --navy-deep: #34496a;
    --navy-mid: #5d7394;
    --sky: #7ba3d6;
    --lime: #dfe35a;
    --lavender: #b7c0e6;
    --white: #ffffff;
    --ink: #1c1f26;
    --teal: #12b3b5;
  }
  * { margin: 0; padding: 0; box-sizing: border-box; }
  html, body {
    width: 1200px; height: 950px; overflow: hidden;
    background: var(--page);
    font-family: "Jost", "Futura", sans-serif;
  }
  .canvas { position: relative; width: 1200px; height: 950px; }

  .card {
    position: absolute;
    width: 516px; height: 315px;
    overflow: hidden;
  }
  .card--front {
    left: 343px; top: 113px;
    background: linear-gradient(90deg, var(--navy-deep) 0%, var(--navy-mid) 45%, #6c84a6 80%, var(--sky) 100%);
  }
  .card--back {
    left: 344px; top: 549px;
    background: linear-gradient(90deg, var(--sky) 0%, #6a86ad 22%, var(--navy-mid) 55%, #3e587a 85%, var(--navy-deep) 100%);
  }

  /* Front */
  .brand {
    position: absolute; right: 27px; top: 92px;
    display: flex; align-items: center; gap: 16px;
  }
  .brand__mark {
    width: 56px; height: 56px;
    background: var(--teal);
  }
  .brand__name {
    color: var(--lime);
    font-weight: 600;
    text-align: right;
    line-height: 1;
    text-transform: uppercase;
  }
  .brand__name .line-main { display: block; font-size: 50px; letter-spacing: 0.5px; }
  .brand__name .line-sub { display: block; font-size: 25px; margin-top: 2px; }

  .front-url {
    position: absolute; left: 0; right: 0; top: 228px;
    text-align: center;
    color: var(--white);
    font-size: 17px; font-weight: 500;
  }
  .tagline {
    position: absolute; left: 29px; right: 29px; top: 263px;
    display: flex; justify-content: space-between;
    color: var(--lavender);
    font-size: 17px; letter-spacing: 7px;
  }

  /* Back */
  .person {
    position: absolute; left: 0; right: 0; top: 31px;
    text-align: center;
  }
  .person__name {
    color: var(--lime);
    font-size: 26px; font-weight: 600;
    letter-spacing: 0.3px;
    line-height: 1.1;
  }
  .person__role {
    color: var(--white);
    font-size: 15.5px; font-weight: 500;
    margin-top: 2px;
  }
  .address {
    position: absolute; left: 0; right: 0; top: 118px;
    text-align: center;
    color: var(--lavender);
    font-size: 13px; line-height: 16px;
    letter-spacing: 0.3px;
  }
  .phones {
    position: absolute; left: 0; right: 0; top: 166px;
    text-align: center;
    color: var(--ink);
    font-size: 19px;
    word-spacing: 1px;
  }
  .phones span + span { margin-left: 14px; }
  .email {
    position: absolute; left: 0; right: 0; top: 195px;
    text-align: center;
    color: var(--lime);
    font-size: 18px;
  }
  .back-url {
    position: absolute; left: 0; right: 0; top: 218px;
    text-align: center;
    color: var(--ink);
    font-size: 18px; font-weight: 500;
  }
  .services {
    position: absolute; left: 0; right: 0; top: 262px;
    text-align: center;
    color: var(--lavender);
    font-size: 14px;
  }
  .services .divider { color: var(--lime); margin: 0 5px; }
</style>
</head>
<body>
<div class="canvas">

  <section class="card card--front">
    <div class="brand">
      <div class="brand__mark"></div>
      <div class="brand__name">
        <span class="line-main">Harlow</span>
        <span class="line-sub">Property Group</span>
      </div>
    </div>
    <p class="front-url">www.harlowproperty.com.au</p>
    <p class="tagline"><span>STRATA</span><span>MANAGEMENT</span><span>SERVICES</span></p>
  </section>

  <section class="card card--back">
    <div class="person">
      <h1 class="person__name">DANIEL HARLOW</h1>
      <p class="person__role">Licensed Strata Manager</p>
    </div>
    <p class="address">PO BOX 48, MAPLE HILLS NSW 2031<br>12/5-19 FINCH STREET ELM PARK NSW 2044</p>
    <p class="phones"><span>T:02 9555 0142</span><span>F: 02 9555 0198</span><span>M:0400 123 678</span></p>
    <p class="email">E: info@harlowproperty.com.au</p>
    <p class="back-url">www.harlowproperty.com.au</p>
    <p class="services">Strata Management<span class="divider">|</span>Community Management<span class="divider">|</span>Property Management</p>
  </section>

</div>
</body>
</html>
```